stationary and business card
varkomo.de - online services platform
Project: stationary and business card
stationary and business card - Internet Services
Creative Brief
Modern
Dipl. Inf. Tobias Wendrich
Luvesor
Ulmenhain Str. 14 70386 Haldenbrunn
tobias.wendrich@mailhafen.de
www.varkomo.de
Please use logo colors, and see the following flyer to fit the style: varkomo.de/flyer.pdf
Für Dienstleister: * Kostenlose reservierungsplatform * Kostengunstige Flyer-Werbung * Kosten und Zeit für Anreise gleich bei Reservierung berechnen * Eigene varkomo.de Subdomain und Web- Seite mit einem SSL Zertifi kat * SMS Benachrichtigungen bei Reservierung 24 h Für Kunden: * 24 Stunden täglich online reservieren (z.B. Arzt, Massage, Friseur, uvm.) * Schnelle Abwicklung * Last-Minute-Preise und Frübucherrabatt möglich * Bewertungssystem für zuverlässige Dienstleister

```html
<!DOCTYPE html>
<html lang="de">
<head>
<meta charset="utf-8">
<title>varkomo.de – Geschäftsausstattung</title>
<link href="https://fonts.googleapis.com/css2?family=Open+Sans:wght@400;600;700&display=swap" rel="stylesheet">
<style>
:root{
  --stage:#1d1e20;
  --blue:#2a9fd6;
  --blue-dark:#1b7fb3;
  --green:#7ab51d;
  --paper:#ffffff;
  --paper-shade:#eef2f5;
  --ink:#4a4f55;
  --ink-soft:#8b9197;
}
*{box-sizing:border-box;margin:0;padding:0}
html,body{width:1200px;height:310px;overflow:hidden;background:var(--stage)}
body{font-family:"Open Sans",Arial,sans-serif;color:var(--ink);position:relative}
.item{position:absolute;box-shadow:0 2px 6px rgba(0,0,0,.55);overflow:hidden}
.brand{display:flex;align-items:center;gap:4px;font-weight:700;color:var(--blue);white-space:nowrap}
.brand .dot{border-radius:50%;background:var(--blue);flex:none}
.brand.light{color:#fff}
.brand.light .dot{background:#fff}
.tagline{font-size:4px;color:var(--ink-soft);letter-spacing:.2px;white-space:nowrap}

/* presentation logo */
.hero-brand{position:absolute;left:18px;top:12px;font-size:34px;color:#fff}
.hero-brand .dot{width:38px;height:38px;background:var(--blue)}

/* business cards */
.card{width:120px;height:62px}
.card.white{background:var(--paper)}
.card.blue{background:linear-gradient(160deg,var(--blue),var(--blue-dark))}
.card .brand{position:absolute;left:8px;top:12px;font-size:12px}
.card .brand .dot{width:11px;height:11px}
.card .band{position:absolute;left:0;right:0;bottom:0;height:14px;background:var(--blue)}
.card .band.green{background:var(--green);height:4px}
.card .name{position:absolute;left:8px;top:6px;font-size:5px;font-weight:700;white-space:nowrap}
.card .lines{position:absolute;left:8px;top:14px;font-size:3.4px;line-height:5px;white-space:nowrap}
.card.blue .name,.card.blue .lines{color:#fff}
.card .col2{left:62px}

/* letterheads */
.letter{width:186px;height:276px;background:var(--paper)}
.letter .brand{position:absolute;left:12px;top:12px;font-size:13px}
.letter .brand .dot{width:12px;height:12px}
.letter .tagline{position:absolute;left:28px;top:28px}
.letter .sender{position:absolute;left:112px;top:10px;font-size:3.6px;line-height:5px;color:var(--ink-soft);white-space:nowrap}
.letter .sender b{color:var(--ink);font-size:4.4px}
.letter .foot{position:absolute;left:0;right:0;bottom:0;height:5px;background:var(--blue)}
.letter.second .brand{left:14px;top:16px}
.letter.second .contact{position:absolute;left:14px;top:34px;font-size:3.4px;line-height:4.6px;color:var(--ink-soft);white-space:nowrap}
.faint-mark{position:absolute;left:42px;top:70px;width:100px;height:100px;border-radius:50%;background:var(--paper-shade)}

/* long envelope and slip */
.envelope-long{left:703px;top:60px;width:222px;height:108px;background:var(--paper)}
.envelope-long .brand{position:absolute;left:12px;top:12px;font-size:12px}
.envelope-long .brand .dot{width:11px;height:11px}
.envelope-long .tagline{position:absolute;left:27px;top:27px}
.envelope-long .stripe{position:absolute;left:0;right:0;bottom:0;height:4px;background:var(--blue)}
.slip{left:703px;top:200px;width:222px;height:80px;background:var(--paper)}
.slip .brand{position:absolute;left:12px;top:12px;font-size:11px}
.slip .brand .dot{width:10px;height:10px}
.slip .addr{position:absolute;left:140px;top:12px;font-size:3.4px;line-height:4.6px;color:var(--ink-soft);white-space:nowrap}
.slip .stripe{position:absolute;left:0;right:0;bottom:0;height:4px;background:var(--green)}

/* envelope backs */
.env-back{left:948px;width:228px;height:104px;background:var(--paper)}
.env-back svg{position:absolute;left:0;top:0}
</style>
</head>
<body>

<div class="brand hero-brand"><span class="dot"></span>varkomo.de</div>

<!-- business cards: fronts -->
<div class="item card white" style="left:20px;top:108px">
  <div class="brand"><span class="dot"></span>varkomo.de</div>
  <div class="band"></div>
</div>
<div class="item card blue" style="left:150px;top:108px">
  <div class="brand light"><span class="dot"></span>varkomo.de</div>
  <div class="band green"></div>
</div>

<!-- business cards: backs -->
<div class="item card white" style="left:20px;top:212px">
  <div class="name">Tobias Wendrich</div>
  <div class="lines">Dipl. Inf.<br>Ulmenhain Str. 14<br>70386 Haldenbrunn</div>
  <div class="lines col2">tobias.wendrich@mailhafen.de<br>www.varkomo.de<br>Tel. 04567 203918</div>
  <div class="band green"></div>
</div>
<div class="item card blue" style="left:150px;top:212px">
  <div class="name">Tobias Wendrich</div>
  <div class="lines">Dipl. Inf.<br>Ulmenhain Str. 14<br>70386 Haldenbrunn</div>
  <div class="lines col2">tobias.wendrich@mailhafen.de<br>www.varkomo.de<br>Tel. 04567 203918</div>
  <div class="band green"></div>
</div>

<!-- letterhead -->
<div class="item letter" style="left:292px;top:12px">
  <div class="brand"><span class="dot"></span>varkomo.de</div>
  <div class="tagline">Online reservieren</div>
  <div class="sender"><b>Luvesor</b><br>Ulmenhain Str. 14<br>70386 Haldenbrunn<br>www.varkomo.de</div>
  <div class="foot"></div>
</div>

<!-- follow-up sheet -->
<div class="item letter second" style="left:500px;top:12px">
  <div class="brand"><span class="dot"></span>varkomo.de</div>
  <div class="contact">tobias.wendrich@mailhafen.de<br>www.varkomo.de</div>
  <div class="faint-mark" role="img" aria-label="Dezentes Markenzeichen als Hintergrund"></div>
</div>

<!-- long envelope -->
<div class="item envelope-long">
  <div class="brand"><span class="dot"></span>varkomo.de</div>
  <div class="tagline">Online reservieren</div>
  <div class="stripe"></div>
</div>

<!-- compliment slip -->
<div class="item slip">
  <div class="brand"><span class="dot"></span>varkomo.de</div>
  <div class="addr">Luvesor · Ulmenhain Str. 14<br>70386 Haldenbrunn<br>www.varkomo.de</div>
  <div class="stripe"></div>
</div>

<!-- envelope backs -->
<div class="item env-back" style="top:60px">
  <svg width="228" height="104" viewBox="0 0 228 104"><polygon points="0,0 228,0 114,50" fill="var(--green)"/></svg>
</div>
<div class="item env-back" style="top:118px">
  <svg width="228" height="104" viewBox="0 0 228 104"><polygon points="0,0 228,0 114,50" fill="var(--blue)"/></svg>
</div>
<div class="item env-back" style="top:178px">
  <svg width="228" height="104" viewBox="0 0 228 104"><polygon points="0,0 228,0 114,50" fill="var(--paper-shade)" stroke="#d6dde2" stroke-width="1"/></svg>
</div>

</body>
</html>
```